Personal Development Model Graphic

I am creating a Personal Development/Coaching business and website and need some assistance with the development of a graphic that represents my methodology. I have already done what I consider to be a working version, but now it's time to have a professional design eye take a look at it and improve.

Specifically, I need assistance on color usage. I'd like each of the 8 areas of the model to have a color, and I've tried to utilize colors I feel are representative of the specific area(for example, purple for spirituality) but it doesn't really work for everything and perhaps additional thought could be put to that aspect of it.

Also, the model needs to work in reverse of the way it's pictured in the attached JPEG. So Friends needs to be first (top center)and then going clockwise, Spirituality needs to be in the 1:00 position not the 11:00 position and then continue around to Community, Family, Exercise, Career, Art/Creativity, and last at 11:00 Sexuality. I was going to update it before uploading, but I'm having trouble with Photoshop and just decided to pull the trigger on having a designer do it.

Thank you in advance for your creativity and ideas!

Industry/Entity Type

Business

Requirements
Nice to have
• It would be fantastic if it could feel modern, and high tech. I realize this is difficult with circles! But whatever you can do.

On color usage, it would again be wonderful to have colors that are more modern than traditional. I'll leave that to your discretion.

```html
<!DOCTYPE html>
<html lang="en">
<head>
<meta charset="utf-8">
<title>Happiness Model</title>
<link rel="stylesheet" href="https://fonts.googleapis.com/css2?family=PT+Sans:wght@700&display=swap">
<style>
  :root {
    --bg: #ffffff;
    --ring-dark: #2b2b2b;
    --label: #ffffff;
    --hub-text: #3a3a3a;
    --friends: #ef5a2a;      --friends-core: #e8402e;
    --spirit: #1f3f8e;       --spirit-core: #1d4a93;
    --community: #1b9bd7;    --community-core: #0b6db4;
    --family: #3cc1d0;       --family-core: #1f90ab;
    --exercise: #0c8ea6;     --exercise-core: #10727a;
    --career: #0f5a4d;       --career-core: #3c6c63;
    --art: #7a3995;          --art-core: #3d1c4b;
    --sexuality: #c3238e;    --sexuality-core: #c62f90;
  }
  html, body { margin: 0; padding: 0; overflow: hidden; background: var(--bg); }
  .canvas { width: 1200px; height: 848px; position: relative; overflow: hidden; }
  .model { display: block; width: 1200px; height: 848px; }
  .area-label {
    font-family: "PT Sans", "Helvetica Neue", Arial, sans-serif;
    font-weight: 700; font-size: 17px; fill: var(--label);
    text-anchor: middle; dominant-baseline: middle;
  }
  .hub-label {
    font-family: "PT Sans", "Helvetica Neue", Arial, sans-serif;
    font-weight: 700; font-size: 46px; fill: var(--hub-text);
    text-anchor: middle; dominant-baseline: middle;
  }
  .core-ring { stroke: var(--ring-dark); stroke-width: 5; }
  .gloss { fill: #ffffff; opacity: 0.14; }
</style>
</head>
<body>
<div class="canvas">
<svg class="model" viewBox="0 0 1200 848" xmlns="http://www.w3.org/2000/svg">
  <defs>
    <linearGradient id="fade-friends" x1="0" y1="1" x2="0" y2="0"><stop offset="0" stop-color="var(--friends)" stop-opacity="0.25"/><stop offset="0.6" stop-color="var(--friends)"/></linearGradient>
    <linearGradient id="fade-spirit" x1="0" y1="1" x2="0" y2="0"><stop offset="0" stop-color="var(--spirit)" stop-opacity="0.25"/><stop offset="0.6" stop-color="var(--spirit)"/></linearGradient>
    <linearGradient id="fade-community" x1="0" y1="1" x2="0" y2="0"><stop offset="0" stop-color="var(--community)" stop-opacity="0.25"/><stop offset="0.6" stop-color="var(--community)"/></linearGradient>
    <linearGradient id="fade-family" x1="0" y1="1" x2="0" y2="0"><stop offset="0" stop-color="var(--family)" stop-opacity="0.3"/><stop offset="0.6" stop-color="var(--family)"/></linearGradient>
    <linearGradient id="fade-exercise" x1="0" y1="1" x2="0" y2="0"><stop offset="0" stop-color="var(--exercise)" stop-opacity="0.3"/><stop offset="0.6" stop-color="var(--exercise)"/></linearGradient>
    <linearGradient id="fade-career" x1="0" y1="1" x2="0" y2="0"><stop offset="0" stop-color="var(--career)" stop-opacity="0.6"/><stop offset="0.6" stop-color="var(--career)"/></linearGradient>
    <linearGradient id="fade-art" x1="0" y1="1" x2="0" y2="0"><stop offset="0" stop-color="var(--art)" stop-opacity="0.2"/><stop offset="0.6" stop-color="var(--art)"/></linearGradient>
    <linearGradient id="fade-sexuality" x1="0" y1="1" x2="0" y2="0"><stop offset="0" stop-color="var(--sexuality)" stop-opacity="0.2"/><stop offset="0.6" stop-color="var(--sexuality)"/></linearGradient>
    <radialGradient id="hub-glow" cx="0.6" cy="0.45" r="0.6">
      <stop offset="0" stop-color="#fff23a"/>
      <stop offset="0.55" stop-color="#fbc62a"/>
      <stop offset="1" stop-color="#f07f22"/>
    </radialGradient>
    <path id="petal" d="M0,-130 L66.5,-290.4 A72,72 0 1 0 -66.5,-290.4 Z"/>
  </defs>

  <!-- Petals -->
  <g class="petals" transform="translate(583 428)">
    <use href="#petal" fill="url(#fade-friends)"/>
    <use href="#petal" fill="url(#fade-spirit)" transform="rotate(45)"/>
    <use href="#petal" fill="url(#fade-community)" transform="rotate(90)"/>
    <use href="#petal" fill="url(#fade-family)" transform="rotate(135)"/>
    <use href="#petal" fill="url(#fade-exercise)" transform="rotate(180)"/>
    <use href="#petal" fill="url(#fade-career)" transform="rotate(225)"/>
    <use href="#petal" fill="url(#fade-art)" transform="rotate(270)"/>
    <use href="#petal" fill="url(#fade-sexuality)" transform="rotate(315)"/>
  </g>

  <!-- Area cores -->
  <g class="cores">
    <circle class="core-ring" cx="583" cy="110" r="60" fill="var(--friends-core)"/>
    <circle class="core-ring" cx="808" cy="203" r="60" fill="var(--spirit-core)"/>
    <circle class="core-ring" cx="901" cy="428" r="60" fill="var(--community-core)"/>
    <circle class="core-ring" cx="808" cy="653" r="60" fill="var(--family-core)"/>
    <circle class="core-ring" cx="583" cy="746" r="60" fill="var(--exercise-core)"/>
    <circle class="core-ring" cx="358" cy="653" r="60" fill="var(--career-core)"/>
    <circle class="core-ring" cx="265" cy="428" r="60" fill="var(--art-core)"/>
    <circle class="core-ring" cx="358" cy="203" r="60" fill="var(--sexuality-core)"/>
  </g>
  <g class="glosses">
    <path class="gloss" d="M525,110 A58,58 0 0 1 641,110 A70,50 0 0 0 525,110 Z"/>
    <path class="gloss" d="M750,203 A58,58 0 0 1 866,203 A70,50 0 0 0 750,203 Z"/>
    <path class="gloss" d="M843,428 A58,58 0 0 1 959,428 A70,50 0 0 0 843,428 Z"/>
    <path class="gloss" d="M750,653 A58,58 0 0 1 866,653 A70,50 0 0 0 750,653 Z"/>
    <path class="gloss" d="M525,746 A58,58 0 0 1 641,746 A70,50 0 0 0 525,746 Z"/>
    <path class="gloss" d="M300,653 A58,58 0 0 1 416,653 A70,50 0 0 0 300,653 Z"/>
    <path class="gloss" d="M207,428 A58,58 0 0 1 323,428 A70,50 0 0 0 207,428 Z"/>
    <path class="gloss" d="M300,203 A58,58 0 0 1 416,203 A70,50 0 0 0 300,203 Z"/>
  </g>

  <!-- Labels -->
  <g class="labels">
    <text class="area-label" x="583" y="101">Friends</text>
    <text class="area-label" x="818" y="197">Spirituality</text>
    <text class="area-label" x="903" y="426">Community</text>
    <text class="area-label" x="813" y="657">Family</text>
    <text class="area-label" x="583" y="747">Exercise</text>
    <text class="area-label" x="357" y="651">Career</text>
    <text class="area-label" x="265" y="412">Art/</text>
    <text class="area-label" x="265" y="434">Creativity</text>
    <text class="area-label" x="358" y="201">Sexuality</text>
  </g>

  <!-- Hub -->
  <g class="hub">
    <circle cx="583" cy="428" r="126" fill="var(--ring-dark)"/>
    <circle cx="583" cy="428" r="117" fill="#8a8a8a"/>
    <circle cx="583" cy="428" r="112" fill="url(#hub-glow)"/>
    <path class="gloss" d="M471,428 A112,112 0 0 1 695,428 A130,90 0 0 0 471,428 Z"/>
    <text class="hub-label" x="583" y="432">Happiness</text>
  </g>
</svg>
</div>
</body>
</html>
```